Blind dating / hook up web

We're creating a new web application based on blind dates to hook up with others who like you (occasional dating, not long-term relationships): www.velvetquorra.com
The background idea is the same as other dating websites (there're many differences but probably don't matter for the design): to browse potential matching profiles based on several criteria (age, gender, zone, etc.) and vote for the ones you like (a yes/no answer just seeing the pictures and basic info, option to see the detailed profile including other users feedback about that profile). The other users do the same, and then, you can see the real matches and contact them.
The one who start the contact to matched profiles, should pay for it, discounting the cost from a previously funded credit balance.
There's also a section to browse for meeting places/plans suggestions.
After you had any date, you could leave feedback about the other, so, everyone had a reputation (similar to the tradlo's feedback system).
Of course, the other typical options: register/mail verification, profile edit, "loading..." stuff, etc.
We'll start with a typical website application, but we'll move to mobile app soon, so, a responsive design will be a plus.

We expect to get a design to use as a pattern to develop (our job) the application, so, we'll need to work with the winning designer to get the graphical pieces/elements (backgrounds, icons, sprites, etc.) not only the whole screen captures. We'll contact the finalists to discuss details about how much of this are included or not and possible future work if we need it.

We've got no previous work done on logos or color schemes, so, feel free to work on whatever you want.

Please, feel free to ask for details if you need more: plinthworksltd@maremail.example

One preference on our web development will be to use Scaffoldr (or similar frameworks), so, if you know about it and you'd like to take in care, this will be a plus, not a must. If you think there will be something to gain on other design patterns, please, forget Scaffoldr and put preference on the design itself.

After received the first drafts, I think there's something general to clarify:

Everybody seem to tend to include several romantic references... the website will not be dedicated to find a long term relationship but occasional affairs, so, maybe hearts aren't the best symbol and romantic pictures/slogans the best resources. 
Also we're searching for a different design/concept than other dating services... there're some key points to make it special (different from typical date websites): 
- Mark potential matching profiles with answering a simply Yes/No (I like / I don't like) 
- Blind dates: you finally don't know who are you going to meet, you just know both answered Yes. So, intrigue will be a better idea than love. 

Let’sfocus a little more what we have in mind to be a different dating site andwhat we expect to obtain with this design project:

The mainfunctionalities and, so, the most important parts to design are:

1. Viewinga sequence of potential matching profiles, answer a question similar to “do youwant to hook up he/she/them?” Clearly more “hot” than “sweet”… more erotic (notX) than love/tender… more prohibited/hidden/secret thanstandard/traditional/public/familiar…

This simplysystem can be the principal idea so, could take a good place in the home,before register showing the best rated profiles, and after register to show thepotential matches.

The sitewon’t be restricted to men/women, it will allow to register as couple too andthe mix of sexual orientations hetero/bi/homo... Of course you should registerand choose your filter parameters, but you’ll do it sometimes, not in everyvisit to the site.

The usershould see a big picture of each profile (this is the first attraction, we’rehooking up not searching for our whole-life partner) and just a few otherdetails like age and feedback rating from other users that already met thatprofile.

Thereshould be a way to review what profiles did you answer Yes and what No.

2. Anotherimportant part of the site is the one to create and propose meet plans. You canpost here your fantasies, your plans, your suggestions about what do you wantto do or what you propose for the meeting. This is where the search engine willtake place, to propose you places, ideas or services based on what you’refinding. This will be some kind of wizard or assistant, to “configure” yourideal meeting. It should suggest you activities to include in your plan and thesearch engine will suggest related places related to that activities. I.e.: ifI’d like to take a dinner, grab some beers and finish the night on a 5 starhotel suite, I’ll add “Dinner ideas”, “going out ideas” and “night stay ideas”(or something similar) and the engine will suggest me some near restaurants,pubs and hotels. Of course, you can enter your personalized plan manually inplain text or just select activities without taking any suggestion. (reserve aplace to suggest new activities to the system!)

Afterconfiguring your plan, you can post it to be realized some days and expose itto your matches to find anyone that like your plan.

This wizardwill allow you to browse the past plans to edit/reuse them and also receiveanswers from the matching profiles who like your plant to initiate the finalcontact and meet them.

3. Inanother section you should see plans posted by others and have the way toaccept or discard them.

4. Ofcourse, the homepage must not be as simple as the Yes/No answering section, it’simportant to explain what the service are and how it works, but, for us, it’smore important to see how the “daily” operative will show up than the home,because the home must be a reflect, a summary, of the operative surrounded bycatching slogans.

There’realso several related or secondary screens and resources to be designed, but,first, we’ll to focus on these four things. Drafts should reflect these ideasor will be very difficult to fit.

After revising a lot of designs sent, there's something we're doing wrong... maybe I'm not explaining myself well, so, let me try again to expose some important ideas and add some others that had appeared after a few designs that I thing they're on the right way:

- the site should be different from the "standard" dating services. Think more in casual meetings, sex encounters, swingers, hot nights, etc. Men, women or couples (even groups!) looking for anything... so, think on any kind of sexual orientation. People live in a stressed society, they're finding something different without loosing time... something spicy, intrigue, surprise, horny... just fun, not love, no sweet, no false promises... but at the same time, think on another way to structure it, another point of view, not the typical Register, browse, contact, meet.
- please, avoid the "register" form directly on the home... the user should take a full free tour all over the site without registering. The site will collect information about his/her/their preferences while he/she/they are looking what the site is about. When clicking on something that really need to be registered, then, the register form will appear already filled with all the collected information. Some kind of remember should appear if the user is using the site for a long time stuck, for example, answering yes/no to the profiles. But there shouldn't be any pressure to register, it should be a natural need after a while.
- The landing homepage should accomplish just three main objectives:
1. Explain what the service are about in just a few sentences (more about it later)
2. Choose your profile type preferences (I'm looking for...): men/women/couples, taking in care that I could find one, two or all three options... and enter to the site to see profiles
3. If I'm already registered, log in.
The login should be easy to see and find, but shouldn't be take too much importance.
The explaining sentences/section should be also easy to see, but can be a scroll down section
The most important and eye-catching should be the selector... with naughty pictures of men/women/couples to mark what you're looking for... maybe a title "What are you looking for?" and a site entrance "Let's hook-up!" that appears after choosing at least one option...
- After the landing homepage, the operational sections described on the previous update... where the backgrounds (and maybe the whole theme) should change according the user preferences... (don't show a women picture if the user isn't looking for women).
Don't think about if the design will end in a very difficult development! it's more important to have a good design and then, our developers will find the way to implement it. Don't be afraid of it! let your talent flow freely ;)

Many of your are using some kind of form to enter the search parameters... We want to try to avoid this and we're thinking on integrate the form on the homepage itself... something like to use icons to select "what I'm" (Man/Woman/Couple... in a similar way as many of you are showing the total profiles of each...); then, a second, bigger, selector to choose "what I'm looking for" (Men/Women/Couples, could select one or many)... maybe playing with big pictures or the background itself; finally (perhaps integrated with the results) some kind of slider to select the age range, leaving only the dropdowns to select the geographic location (if no one has a better idea with no typical "fields").

Reason: Some of you are in a very good way, but probably you need some more time to make your ideas shine ;)

```html
<!DOCTYPE html>
<html lang="en">
<head>
<meta charset="utf-8">
<title>Plinthworks Ltd — Dating</title>
<link href="https://fonts.googleapis.com/css2?family=Open+Sans:ital,wght@0,400;0,600;0,700;1,400&family=Roboto+Slab:wght@400&family=Roboto:wght@400;500&display=swap" rel="stylesheet">
<style>
:root{
  --pink:#e8125f;
  --pink-dark:#c40f50;
  --teal:#1a6a8a;
  --teal-btn:#1d8fb8;
  --ink:#333;
  --muted:#777;
  --light-band:#e6edf5;
  --grey-band:#f5f5f5;
  --dark-band:#333;
  --footer:#222;
  --white:#fff;
}
*{box-sizing:border-box;margin:0;padding:0}
html,body{width:1200px;height:2866px;overflow:hidden}
body{font-family:"Open Sans",Arial,sans-serif;color:var(--ink);background:var(--white);position:relative}
.abs{position:absolute}

/* Hero */
.hero{position:absolute;left:0;top:0;width:1200px;height:625px;
  background:linear-gradient(180deg,#a9c6de 0%,#cfdbe4 18%,#5e8fa8 26%,#7a99a6 32%,#b9a88c 48%,#8d7b66 70%,#4e4540 100%);
  border-bottom:3px solid #ccc}
.brand{position:absolute;left:109px;top:0;width:288px;height:130px}
.brand svg{position:absolute;left:0;top:0}
.brand-name{position:absolute;left:0;top:30px;width:288px;text-align:center;
  font-weight:700;font-size:30px;color:var(--pink);letter-spacing:1px;display:flex;align-items:center;justify-content:center;gap:10px}
.brand-name i{display:inline-block;width:16px;height:16px;border-radius:50%;background:var(--pink)}

.search{position:absolute;left:109px;top:214px;width:323px;height:325px;background:#111}
.search h2{background:var(--pink);color:#fff;font-weight:600;font-size:20px;height:40px;line-height:40px;padding-left:13px}
.search .row{position:absolute;left:13px;width:300px;height:34px;display:flex;align-items:center}
.search label{color:#fff;font-size:13px;font-weight:600;width:84px}
.search .field{width:205px;height:34px;background:#fff;border-radius:2px}
.search .btn{position:absolute;left:13px;top:252px;width:296px;height:50px;border-radius:3px;
  background:linear-gradient(#2aa7d2,#177fa6);color:#fff;font-size:24px;font-weight:600;text-align:center;line-height:50px}

/* Section headings */
.title{position:absolute;left:0;width:1200px;text-align:center;font-weight:700;text-transform:uppercase}
.sub{position:absolute;left:0;width:1200px;text-align:center;font-style:italic;font-size:14px}

/* Suggestions */
.card{position:absolute;left:120px;top:751px;width:163px;height:233px;background:#2a2a2a;border:1px solid #111}
.card .b{position:absolute;left:25px;width:113px;height:37px;color:#fff;font-size:14px;text-align:center;line-height:37px}
.b.detail{top:56px;border:1px solid #bbb;background:#3a3a3a}
.b.yes{top:103px;background:#a8143f}
.b.no{top:149px;background:#1e5d73}
.card .ghost{position:absolute;left:0;top:190px;width:163px;text-align:center;font-family:"Roboto Slab",serif;font-size:13px;color:#444}
.member{position:absolute;top:789px;width:130px;height:130px;border-radius:50%;border:3px solid #ddd;
  background:radial-gradient(circle at 50% 40%,#c8b2a0,#7d6b60 70%,#e8e4de)}
.mname{position:absolute;top:940px;width:200px;text-align:center;font-family:"Roboto Slab",serif;font-size:13px;color:var(--teal);text-transform:uppercase}

/* Find singles */
.singles{position:absolute;left:0;top:1061px;width:1200px;height:311px;background:var(--light-band)}
.singles p{position:absolute;left:138px;top:162px;width:925px;text-align:center;font-size:15px;line-height:22px;color:#777}

/* Options */
.opt{position:absolute;top:1586px;width:320px;text-align:center}
.opt svg{display:block;margin:0 auto;height:112px}
.opt h3{margin-top:28px;font-size:16px;font-weight:400;color:#444;text-transform:uppercase}
.opt p{margin:8px auto 0;width:270px;font-size:15px;line-height:21px;color:#444}

/* About */
.about{position:absolute;left:0;top:1882px;width:1200px;height:564px;background:var(--grey-band)}
.tabs{position:absolute;left:120px;top:142px;display:flex;gap:11px}
.tab{height:36px;border:2px solid #ddd;border-bottom:none;background:#f5f5f5;font-family:Roboto,Arial,sans-serif;font-size:13px;color:#aaa;text-transform:uppercase;line-height:34px;text-align:center;border-radius:3px 3px 0 0}
.tab.active{background:#fff;color:#555}
.panel{position:absolute;left:120px;top:178px;width:960px;height:327px;background:#fff;border:2px solid #ddd;border-radius:0 3px 3px 3px;font-family:Roboto,Arial,sans-serif;font-size:12px;color:#444}
.panel .lead{position:absolute;left:20px;top:20px}
.panel ul{position:absolute;left:20px;list-style:none}
.panel li{line-height:19px;padding-left:16px;position:relative}
.panel li::before{content:"";position:absolute;left:2px;top:8px;width:4px;height:4px;border-radius:50%;background:#aaa}
.panel .rule{position:absolute;left:20px;width:916px;height:1px;background:#ddd}
.panel .quote{position:absolute;left:0;top:214px;width:956px;text-align:center;font-style:italic;color:#aaa;font-size:13px}
.panel .reg{position:absolute;left:419px;top:271px;width:116px;height:39px;background:var(--pink);color:#fff;font-size:13px;font-weight:500;text-align:center;line-height:39px;text-transform:uppercase}

/* Contact */
.contact{position:absolute;left:0;top:2446px;width:1200px;height:375px;background:var(--dark-band)}
.input{position:absolute;background:#2a2a2a;border:1px solid #222;border-radius:3px;color:#666;font-size:13px;padding-left:14px;line-height:33px}
.send{position:absolute;left:963px;top:289px;width:119px;height:38px;background:var(--pink);color:#fff;font-weight:700;font-size:14px;text-align:center;line-height:38px}
.footer{position:absolute;left:0;top:2821px;width:1200px;height:45px;background:var(--footer);color:#ddd;font-size:14px;text-align:center;line-height:45px}
</style>
</head>
<body>

<header class="hero" role="img" aria-label="Photograph of a couple lying together on rocks at a beach, sea and sky behind">
  <div class="brand">
    <svg width="288" height="130" viewBox="0 0 288 130"><path d="M0 0H288V108L144 130L0 108Z" fill="#fff"/><path d="M0 108L144 130L288 108" fill="none" stroke="var(--pink)" stroke-width="5"/></svg>
    <div class="brand-name"><i></i>PLINTHWORKS</div>
  </div>
  <form class="search" role="search">
    <h2>Search Members</h2>
    <div class="row" style="top:63px"><label>I am a &nbsp;&nbsp;:</label><span class="field"></span></div>
    <div class="row" style="top:109px"><label>Seeking a :</label><span class="field"></span></div>
    <div class="row" style="top:155px"><label>Country &nbsp;&nbsp;:</label><span class="field"></span></div>
    <div class="row" style="top:201px"><label>Zip Code :</label><span class="field"></span></div>
    <div class="btn">Search</div>
  </form>
</header>

<section>
  <h2 class="title" style="top:672px;font-size:42px;color:var(--pink)">Suggestions</h2>
  <p class="sub" style="top:730px;color:var(--teal)">Most online members</p>
  <div class="card">
    <div class="b detail">Detail</div>
    <div class="b yes">YES</div>
    <div class="b no">NO</div>
    <div class="ghost">LANISA</div>
  </div>
  <div class="member" role="img" aria-label="Profile photo of John Doe" style="left:296px"></div>
  <div class="member" role="img" aria-label="Profile photo of Jessica Doe" style="left:455px"></div>
  <div class="member" role="img" aria-label="Profile photo of Jason Da Vinci" style="left:615px"></div>
  <div class="member" role="img" aria-label="Profile photo of Maya Stattam" style="left:776px"></div>
  <div class="member" role="img" aria-label="Profile photo of Michael Doe" style="left:934px"></div>
  <div class="mname" style="left:261px">John Doe</div>
  <div class="mname" style="left:420px">Jessica Doe</div>
  <div class="mname" style="left:580px">Jason Da Vinci</div>
  <div class="mname" style="left:741px">Maya Stattam</div>
  <div class="mname" style="left:899px">Michael Doe</div>
</section>

<section class="singles">
  <h2 class="title" style="top:48px;font-size:40px;color:var(--teal)">Find Singles</h2>
  <p class="sub" style="top:104px;color:var(--pink)">That just want to have fun</p>
  <p>Sed ut perspiciatis unde omnis iste natus error sit voluptatem accusantium doloremque laudantium, totam rem aperiam, eaque ipsa quae ab illo inventore veritatis et quasi architecto beatae vitae dicta sunt explicabo. Nemo enim ipsam voluptatem quia voluptas sit aspernatur aut odit aut fugit, sed quia consequuntur magni dolores eos qui ratione voluptatem sequi nesciunt. Neque porroquisquam est, qui dolorem ipsum quia dolor sit amet, consectetur, adipisci velit, sed quia non numquam modi tempora.</p>
</section>

<section>
  <h2 class="title" style="top:1428px;font-size:42px;font-weight:400;color:var(--pink)">Amazing options of our dating website</h2>
  <p class="sub" style="top:1494px;color:var(--teal)">Join free to start</p>
  <div class="opt" style="left:121px">
    <svg viewBox="0 0 70 112" width="70"><circle cx="35" cy="33" r="27" fill="none" stroke="var(--pink)" stroke-width="5"/><path d="M35 60V110M16 86H54" stroke="var(--pink)" stroke-width="5"/></svg>
    <h3>Single Girls</h3>
    <p>Lorem ipsum consectetur adipisicing sed do eiusmod tempor incididunt &nbsp;labore dolore magna aliqua.</p>
  </div>
  <div class="opt" style="left:440px">
    <svg viewBox="0 0 190 112" width="190"><path d="M78 104C60 90 12 70 8 40C5 18 22 6 38 10C52 13 58 26 60 32C64 24 74 12 88 16C104 20 108 40 100 60C94 76 84 92 78 104Z" fill="none" stroke="var(--teal)" stroke-width="5"/><path d="M118 96C110 82 108 66 114 50C118 40 128 34 138 40C142 44 144 48 144 52C150 44 160 40 170 44C182 50 184 66 172 76C160 86 140 92 118 96Z" fill="none" stroke="var(--pink)" stroke-width="5"/></svg>
    <h3>We are connecting singles</h3>
    <p>Lorem ipsum consectetur adipisicing sed do eiusmod tempor incididunt &nbsp;labore dolore magna aliqua.</p>
  </div>
  <div class="opt" style="left:757px">
    <svg viewBox="0 0 100 112" width="100"><circle cx="36" cy="66" r="28" fill="none" stroke="var(--teal)" stroke-width="5"/><path d="M56 46L88 14M64 12H90V38" fill="none" stroke="var(--teal)" stroke-width="5"/></svg>
    <h3>Single Men</h3>
    <p>Lorem ipsum consectetur adipisicing sed do eiusmod tempor incididunt &nbsp;labore dolore magna aliqua.</p>
  </div>
</section>

<section class="about">
  <h2 class="title" style="top:30px;font-size:40px;color:#333">About Us</h2>
  <p class="sub" style="top:86px;color:#999">find something more about our dating service</p>
  <div class="tabs">
    <div class="tab active" style="width:141px">Register Free</div>
    <div class="tab" style="width:115px">Find Dates</div>
    <div class="tab" style="width:246px">Singles are waiting for you</div>
    <div class="tab" style="width:147px">Privacy Policy</div>
  </div>
  <div class="panel">
    <p class="lead">Lorem ipsum dolor sit amet, consectetur adipisicing elit. Consequatur et ducimus quaerat quidem rerum dolorem velit repudiandae tempore itaque ex.</p>
    <ul style="top:58px"><li>Nam nec tellus cursus eter</li><li>Ga odio tincidunt auctor ar</li><li>Ornare odioed non nec nigib odio</li></ul>
    <ul style="top:130px"><li>Nam nec tellus cursus eter</li><li>Ga odio tincidunt auctor ar</li><li>Ornare odioed non nec nigib odio</li></ul>
    <div class="rule" style="top:200px"></div>
    <p class="quote">"Lorem ipsum dolor sit amet."</p>
    <div class="rule" style="top:251px"></div>
    <div class="reg">Register</div>
  </div>
</section>

<section class="contact">
  <h2 class="title" style="top:40px;font-size:40px;color:#fff">Contact Us</h2>
  <p class="sub" style="top:96px;color:#999">every day, every week working for you</p>
  <div class="input" style="left:122px;top:147px;width:470px;height:35px">Name</div>
  <div class="input" style="left:122px;top:193px;width:470px;height:35px">Email</div>
  <div class="input" style="left:122px;top:239px;width:470px;height:35px">Subject</div>
  <div class="input" style="left:612px;top:147px;width:470px;height:127px">Message</div>
  <div class="send">SEND</div>
</section>

<footer class="footer">Copy rigthe 2014 © Plinthworks All rights reserved</footer>
</body>
</html>
```